Change of Address Card

We are fertility physicians in New York . Need a change of address postcard .

The front should be colorful
contain the statement " we are moving!"
and the names Lorenzo Bettuni MD, Oksana Dremova MD

Also the front should contain the drawing of a sperm with either wings or wheeels or whatever your creativity suggests as long as it is not vulgar ( we are doctors !)

The back should contain
the address area and stamp area
and a text area
and possibly a recall of the drawing in front.
use same font

text below

Dear Friends and Colleagues

Lorenzo and Oksana are relocating their fertility practice to a new location on 418 West 71st Street, Suite 604, New York NY 10023
Please take note of our new phone number
Our New phone Number is 212-555-0194

Thank you for your support!

Target Market(s)

this is a card that goes to physicians

Industry/Entity Type

It Support

Requirements
Must have
• fit standard postcard size
Rectangular
At least 3-1/2 inches high x 5 inches long x 0.007 inch thick
No more than 4-1/4 inches high x 6 inches long x 0.016 inches thick
will not be mailed in an envelope

```html
<!DOCTYPE html>
<html lang="en">
<head>
<meta charset="utf-8">
<title>We Are Moving – Change of Address Postcard</title>
<link href="https://fonts.googleapis.com/css2?family=Questrial&family=Permanent+Marker&display=block" rel="stylesheet">
<style>
  :root {
    --page: #ffffff;
    --card: #e9e9eb;
    --card-edge: #8e8e90;
    --ink: #1b1b1b;
    --label: #a9a9ab;
    --rule: #6d6d6f;
    --accent-blue: #2aa4dc;
    --illus-light: #f4f4f6;
    --illus-mid: #d2d3d6;
  }
  * { box-sizing: border-box; margin: 0; padding: 0; }
  html, body {
    width: 800px; height: 1200px; overflow: hidden;
    background: var(--page);
  }
  body { position: relative; font-family: "Questrial", "Century Gothic", sans-serif; color: var(--ink); }

  .side-label {
    position: absolute; left: 0; width: 800px; text-align: center;
    font-size: 17px; letter-spacing: 3px; color: var(--label); line-height: 1;
  }
  .side-label--front { top: 3px; }
  .side-label--back { top: 588px; left: -10px; }

  .card {
    position: absolute; left: 0; width: 800px; height: 560px;
    background: var(--card); border: 1px solid var(--card-edge);
  }
  .card--front { top: 23px; }
  .card--back { top: 608px; }

  .hand {
    font-family: "Permanent Marker", "Comic Sans MS", "Chalkboard SE", cursive;
    font-weight: 400;
  }

  /* front */
  .doctors {
    position: absolute; top: 100px; left: 0; width: 800px; text-align: center;
    font-size: 23px; line-height: 30px; white-space: nowrap;
  }
  .doctors b { font-weight: 700; -webkit-text-stroke: 0.6px var(--ink); }
  .doctors .dot {
    display: inline-block; width: 11px; height: 11px; border-radius: 50%;
    background: var(--ink); margin: 0 20px; vertical-align: middle;
  }
  .doctors-rule {
    position: absolute; top: 138px; left: 67px; width: 666px; height: 1px; background: var(--rule);
  }
  .mascot {
    position: absolute; border-radius: 50%;
    background: radial-gradient(ellipse at 62% 38%,
      var(--illus-light) 0 18%,
      var(--accent-blue) 26% 36%,
      var(--illus-mid) 50%,
      var(--card) 70%);
  }
  .mascot--front { left: 295px; top: 188px; width: 210px; height: 190px; }
  .headline {
    position: absolute; top: 440px; left: 0; width: 800px; text-align: center;
    font-size: 58px; line-height: 1; letter-spacing: 3px;
    transform: skewX(-6deg); white-space: nowrap;
  }

  /* back */
  .address-lines { position: absolute; left: 30px; top: 50px; width: 268px; }
  .address-lines span { display: block; height: 1px; background: var(--rule); margin-bottom: 29px; }
  .stamp-box {
    position: absolute; left: 642px; top: 20px; width: 136px; height: 108px;
    border: 1px dashed var(--rule);
  }
  .divider { position: absolute; left: 329px; top: 150px; width: 1px; height: 382px; background: var(--rule); }
  .mascot--back { left: 58px; top: 232px; width: 220px; height: 200px; }

  .message { position: absolute; left: 354px; top: 165px; width: 420px; font-size: 18px; line-height: 23px; }
  .message p { margin-bottom: 20px; }
  .message .greeting { margin-bottom: 21px; }
  .message .new-address {
    font-size: 20px; line-height: 23px;
    text-transform: uppercase; letter-spacing: 1px; margin-bottom: 20px;
  }
  .message .new-phone {
    font-size: 25px; line-height: 28px; letter-spacing: 1.5px; margin-bottom: 16px;
  }
</style>
</head>
<body>
  <div class="side-label side-label--front">FRONT</div>
  <section class="card card--front">
    <div class="doctors">Lorenzo <b>Bettuni</b> MD<span class="dot"></span>Oksana <b>Dremova</b> MD</div>
    <div class="doctors-rule"></div>
    <div class="mascot mascot--front" role="img" aria-label="Cartoon illustration of a cheerful swimming sperm wearing blue goggles, with motion puffs behind it"></div>
    <h1 class="headline hand">WE ARE MOVING!</h1>
  </section>

  <div class="side-label side-label--back">BACK</div>
  <section class="card card--back">
    <div class="address-lines"><span></span><span></span><span></span></div>
    <div class="stamp-box"></div>
    <div class="mascot mascot--back" role="img" aria-label="Cartoon illustration of a cheerful swimming sperm wearing blue goggles, with motion puffs behind it"></div>
    <div class="divider"></div>
    <div class="message">
      <p class="greeting">Dear Friends and Colleagues,</p>
      <p>Lorenzo and Oksana are relocating their<br>fertility practice to a new location on:</p>
      <p class="new-address hand">Suite 604<br>418 West 71st Street<br>New York NY 10023</p>
      <p>*Please take note of our new phone number*</p>
      <p>Our New Phone Number is:</p>
      <p class="new-phone hand">212-555-0194</p>
      <p>Thank you for your support!</p>
    </div>
  </section>
</body>
</html>
```